Business Improvement Consultancy needs web design

I need a web design for my company, that offers support to manufacturing and distribution businesses.

We have worked with a range of organisations to help them get more out of their operational processes and supply chains.

With full end to end supply chain knowledge we help them identify waste in their supply chains that often get overlooked.

We support through a number of offerings

Developing an end to end supply chain strategy

Applying Lean to support the strategy

Interim support network to deliver quick wins and rapid cost improvement

Project Management

Interactive training tools for delivering supply chain best practice.

I have the logos done already, so it is more about look and feel, and the colour schemes etc giving a professional feel.

Also have the web domains www.veltrisgroup.co, www.veltrisgroup.co.uk & www.veltrisgroup.eu, using Q&Z beginner package

Target Market(s)

Manufacturing and distribution businesses, potentially other consultancies looking for collaboration

Industry/Entity Type

Business

Requirements
Must have
• Some pictures on related to performance improvement, bar charts showing productivity growth / increase.

Should have the facebook twitter and linkedin logos to share the website

```html
<!DOCTYPE html>
<html lang="en">
<head>
<meta charset="utf-8">
<title>Veltris Group</title>
<link href="https://fonts.googleapis.com/css2?family=Ubuntu:ital,wght@0,400;0,500;1,400&family=Arimo:wght@400;700&display=swap" rel="stylesheet">
<style>
:root{
  --ink:#2d2c6e;
  --ink-dark:#252449;
  --band:#5b4b7a;
  --panel:#f3f4f6;
  --page-top:#f6f6f7;
  --page-bottom:#e6e7ea;
  --text:#5a5a5a;
  --nav-text:#5e5e5e;
  --rule:#dcdde2;
  --link:#2f74cf;
  --hero-a:#403d84;
  --hero-b:#120f48;
}
*{margin:0;padding:0;box-sizing:border-box}
html,body{width:1200px;height:985px;overflow:hidden}
body{position:relative;background:linear-gradient(var(--page-top),var(--page-bottom) 18%,var(--page-top) 60%,var(--page-bottom));font-family:"Arimo",Arial,sans-serif;color:var(--text)}
.band{position:absolute;left:0;top:178px;width:1200px;height:331px;background:var(--band)}
.brand{position:absolute;left:147px;top:36px;display:flex;align-items:center;gap:14px}
.brand-dot{width:22px;height:22px;border-radius:50%;background:var(--ink)}
.brand-name{font-family:"Ubuntu",sans-serif;font-size:23px;color:var(--ink)}
.phone{position:absolute;left:796px;top:46px;display:flex;align-items:center;gap:16px}
.phone-number{font-family:"Ubuntu",sans-serif;font-weight:500;font-size:28px;letter-spacing:1px;color:var(--ink-dark)}
.panel{position:absolute;left:142px;top:117px;width:914px;height:830px;background:var(--panel);border-radius:4px;box-shadow:0 0 3px rgba(0,0,0,.18)}
.nav{position:absolute;left:142px;top:117px;width:914px;height:46px;display:flex;background:linear-gradient(#fafafa,#e9eaec);border-radius:4px 4px 0 0;border-bottom:1px solid #d8d9dd}
.nav a{display:flex;align-items:center;justify-content:center;font-family:"Ubuntu",sans-serif;font-style:italic;font-size:14px;color:var(--nav-text);text-decoration:none;border-right:1px solid #d3d4d8}
.nav a:last-child{border-right:0}
.hero{position:absolute;left:163px;top:179px;width:871px;height:329px;border:1px solid #cfd0d6;border-radius:4px;overflow:hidden;display:flex;background:#fff}
.hero-copy{width:311px;height:100%;background:linear-gradient(var(--hero-a),var(--hero-b));padding:18px 12px 0 13px;color:#fff;font-family:"Ubuntu",sans-serif;font-size:21px;line-height:23px}
.hero-dots{margin:20px 0 22px;border-top:3px dotted #fff;height:0}
.hero-photo{flex:1;background:linear-gradient(120deg,#e8ecf2,#ffffff 40%,#d9dde4 75%,#2a2c36)}
.divider{position:absolute;left:142px;top:542px;width:914px;height:1px;background:var(--rule)}
.intro{position:absolute;left:164px;top:564px;width:540px}
.intro h1{font-family:"Ubuntu",sans-serif;font-weight:400;font-size:27px;color:var(--ink);margin-bottom:20px}
.intro p{font-size:11.5px;line-height:17px}
.intro .gap{margin-top:17px}
.news{position:absolute;left:781px;top:564px;width:253px}
.news h2{font-family:"Ubuntu",sans-serif;font-weight:400;font-size:27px;color:var(--ink)}
.news-date{font-family:"Ubuntu",sans-serif;font-size:16px;color:#222;margin:2px 0 6px 1px}
.news-photo{width:250px;height:86px;border:1px solid #c9cad0;background:linear-gradient(#f4f4f6,#dcdde0)}
.news p{font-size:11.5px;line-height:17px;margin:14px 0 6px 3px}
.news a{font-size:12px;font-weight:700;color:var(--link);text-decoration:none;margin-left:5px}
.footer{position:absolute;top:960px;left:0;width:1126px;text-align:center;font-size:11.5px;color:#555}
</style>
</head>
<body>
<div class="band"></div>

<header>
  <div class="brand"><span class="brand-dot"></span><span class="brand-name">Veltris Group</span></div>
  <div class="phone">
    <svg width="30" height="22" viewBox="0 0 30 22" aria-hidden="true">
      <path d="M2 7c0-4 6-6 13-6s13 2 13 6v2h-7V6H9v3H2z" fill="#3a3850"/>
      <rect x="5" y="10" width="20" height="11" rx="2" fill="#3a3850"/>
      <circle cx="15" cy="15.5" r="3" fill="#f3f3f4"/>
    </svg>
    <span class="phone-number">555-0142-0198</span>
  </div>
</header>

<div class="panel"></div>

<nav class="nav">
  <a href="#" style="width:151px">Home</a>
  <a href="#" style="width:175px">Supply Chain</a>
  <a href="#" style="width:131px">Lean</a>
  <a href="#" style="width:143px">Interim</a>
  <a href="#" style="width:171px">Contact Us</a>
  <a href="#" style="width:143px">Projects</a>
</nav>

<section class="hero">
  <div class="hero-copy">
    <p>It is a long established fact that a reader will be distracted by the readable content of a page when looking at its layout.</p>
    <div class="hero-dots"></div>
    <p>It is a long established fact that a reader will be distracted by the readable content of a page when looking at its layout.</p>
  </div>
  <div class="hero-photo" role="img" aria-label="Photo of three smiling colleagues in an office looking at a computer monitor"></div>
</section>

<div class="divider"></div>

<main class="intro">
  <h1>Veltris - to improve, to enhance</h1>
  <p>Welcome to Veltris Group. We have worked with a range of organisations to help them get more out of their operational processes and supply chains.<br>
  With full end to end supply chain knowledge we can help you identify waste in your supply chains that often get overlooked.<br>
  Before you look to embark on cost reduction plans or a lean journey, get in touch to ensure that your chosen path delivers sustainability and profitable growth.</p>
  <p class="gap">Please click on the above tabs for more details on how we can help with:</p>
  <p class="gap">Developing an end to end supply chain strategy</p>
  <p class="gap">Applying Lean to support the strategy</p>
  <p class="gap">Interim support network to deliver quick wins and rapid cost improvement</p>
  <p class="gap">Project Management</p>
</main>

<aside class="news">
  <h2>Latest News</h2>
  <div class="news-date">18-09-2011</div>
  <div class="news-photo" role="img" aria-label="Illustration of business people assembling large jigsaw puzzle pieces"></div>
  <p>It is a long established fact that a reader will be distracted by the readable content of a page</p>
  <a href="#">+Read More</a>
</aside>

<footer class="footer">Copyright © 2011 VeltrisGroup. All rights Reserved</footer>
</body>
</html>
```